Letterhead Design Project

Standard A4 paper, center the name Brightway Wash (with the mop) same as front of business card.
47 Harbour Vale Rd Kelston 5062 ABN: 71205839416
M. 0427163958 T. 83917605 Calibri font

Industry/Entity Type

Business

```html
<!DOCTYPE html>
<html lang="en">
<head>
<meta charset="utf-8">
<title>Brightway Wash — Stationery</title>
<link rel="stylesheet" href="https://fonts.googleapis.com/css2?family=Carlito:wght@400;700&display=swap">
<style>
  :root {
    --backdrop: #eef0f1;
    --paper: #ffffff;
    --brand-green: #7ef53a;
    --brand-teal: #5fe6cf;
    --ink-grey: #8a8f93;
    --card-ink: #ffffff;
    --shadow: 0 6px 18px rgba(60, 70, 80, 0.12);
  }
  * { box-sizing: border-box; margin: 0; padding: 0; }
  html, body {
    width: 1200px;
    height: 795px;
    overflow: hidden;
    background: var(--backdrop);
    font-family: "Carlito", Calibri, "Segoe UI", sans-serif;
  }
  .canvas {
    position: relative;
    width: 1200px;
    height: 795px;
  }

  /* Letterhead (A4 proportion) */
  .letterhead {
    position: absolute;
    left: 110px;
    top: 40px;
    width: 505px;
    height: 714px;
    background: var(--paper);
    box-shadow: var(--shadow);
    border-top: 5px solid var(--brand-teal);
    border-bottom: 5px solid var(--brand-green);
  }
  .letterhead .wordmark {
    position: absolute;
    top: 48px;
    left: 0;
    right: 0;
    text-align: center;
    font-size: 24px;
  }
  .letterhead-footer {
    position: absolute;
    right: 36px;
    bottom: 28px;
    display: flex;
    gap: 28px;
    font-size: 8px;
    line-height: 1.5;
    color: var(--ink-grey);
  }
  .label { color: var(--brand-green); font-weight: 700; }

  /* Shared wordmark */
  .wordmark {
    font-weight: 700;
    color: var(--brand-green);
    letter-spacing: 0.01em;
  }

  /* Business cards */
  .card {
    position: absolute;
    left: 690px;
    width: 400px;
    height: 235px;
    box-shadow: var(--shadow);
  }
  .card-front {
    top: 110px;
    background: var(--paper);
    display: flex;
    align-items: center;
    justify-content: center;
  }
  .card-front .wordmark { font-size: 36px; }

  .card-back {
    top: 420px;
    background: var(--brand-green);
    padding: 34px 36px;
    color: var(--card-ink);
  }
  .card-back .wordmark {
    color: var(--card-ink);
    font-size: 26px;
  }
  .card-contact {
    margin-top: 30px;
    font-size: 11px;
    line-height: 1.6;
  }
  .card-contact .label { color: var(--card-ink); }
</style>
</head>
<body>
<main class="canvas">

  <section class="letterhead" aria-label="Letterhead">
    <p class="wordmark">Brightway Wash</p>
    <footer class="letterhead-footer">
      <div class="footer-address">
        <p>47 Harbour Vale Rd Kelston 5062</p>
        <p><span class="label">ABN</span> 71205839416</p>
      </div>
      <div class="footer-phones">
        <p><span class="label">M.</span> 0427163958</p>
        <p><span class="label">T.</span> 83917605</p>
      </div>
    </footer>
  </section>

  <section class="card card-front" aria-label="Business card front">
    <p class="wordmark">Brightway Wash</p>
  </section>

  <section class="card card-back" aria-label="Business card back">
    <p class="wordmark">Brightway Wash</p>
    <div class="card-contact">
      <p>47 Harbour Vale Rd Kelston 5062</p>
      <p><span class="label">ABN</span> 71205839416</p>
      <p><span class="label">M.</span> 0427163958</p>
      <p><span class="label">T.</span> 83917605</p>
    </div>
  </section>

</main>
</body>
</html>
```